Business Card - The Harborline Group

We need a business card for a new venture capital fund and innovation accelerator based in San Francisco, CA. The Harborline Group will back, fund and scale life-transforming businesses. We intend to provide capital along with strategic and tactical direction to teams running exponential organizations. We are backing great ideas for vast markets with passionate visionaries. We facilitate the rapid creation of life-transforming businesses, help invent or re-invent critical industries and move the frontier of progress for the good of humankind. Maplecrest University defines Exponential Organizations as those whose impact (cost reduction or output) is disproportionally large – at least 10x larger – compared to its peers because of the use of new organizational techniques that leverage accelerating technologies. ExOs are characterized by a massive transformative purpose (MTP), a skunkworks organization and passionate teams of brilliant mountain-climbers with technical backgrounds.

Industry/Entity Type

Business

Contact Information for Business Card

Peter Odell
Managing Director

peter@theharborlinegroup.com
+1.628.307.4190

Font styles to use
Sans Serif

Requirements
Must have
• - logo
• - website: www.theharborlinegroup.com

```html
<!DOCTYPE html>
<html lang="en">
<head>
<meta charset="utf-8">
<title>The Harborline Group – Business Card</title>
<link href="https://fonts.googleapis.com/css2?family=Lato:wght@400;700;900&display=swap" rel="stylesheet">
<style>
  :root {
    --backdrop: #2a2a2a;
    --card: #f2f2f2;
    --brand-blue: #2f6597;
    --brand-green: #66a11c;
    --ink: #3b3b3b;
    --ink-soft: #7a7a7a;
    --white: #ffffff;
  }
  * { margin: 0; padding: 0; box-sizing: border-box; }
  html, body {
    width: 1200px; height: 873px; overflow: hidden;
    background: var(--backdrop);
    font-family: "Lato", Arial, sans-serif;
  }
  .card {
    position: absolute; left: 150px; top: 180px;
    width: 900px; height: 514px;
    background: linear-gradient(160deg, var(--white), var(--card));
    box-shadow: 0 10px 30px rgba(0,0,0,.5);
    overflow: hidden;
  }
  .name-band {
    position: absolute; left: 0; right: 0; top: 24px; height: 62px;
    background: var(--brand-blue);
    display: flex; align-items: center; padding-left: 200px; gap: 16px;
  }
  .name-band__name { color: var(--white); font-weight: 900; font-size: 36px; line-height: 1; }
  .name-band__title { color: var(--white); font-size: 15px; margin-top: 4px; }

  .brand {
    position: absolute; left: 205px; top: 170px;
    display: flex; align-items: center; gap: 30px;
  }
  .brand__mark {
    width: 140px; height: 140px; border-radius: 50%;
    background: var(--brand-green); flex: none;
  }
  .brand__text { display: flex; flex-direction: column; gap: 12px; }
  .brand__name {
    font-weight: 900; font-size: 38px; color: var(--ink);
    text-transform: uppercase; letter-spacing: 1px; line-height: 1.05;
  }
  .brand__tagline {
    font-size: 12px; color: var(--ink-soft); letter-spacing: 1.5px;
    text-transform: uppercase; line-height: 1.4;
  }

  .contact-icons {
    position: absolute; left: 0; right: 0; top: 362px; height: 28px;
  }
  .contact-icons svg { position: absolute; top: 0; }
  .contact-band {
    position: absolute; left: 0; right: 0; top: 400px; height: 58px;
    background: var(--brand-green);
  }
  .contact-band__item {
    position: absolute; top: 50%; transform: translateY(-50%);
    color: var(--white); font-weight: 700; font-size: 20px; white-space: nowrap;
  }
  .contact-band__phone { left: 40px; }
  .contact-band__email { left: 255px; }
  .contact-band__web { right: 40px; }
</style>
</head>
<body>
  <main class="card">
    <header class="name-band">
      <span class="name-band__name">Peter Odell</span>
      <span class="name-band__title">Director</span>
    </header>

    <section class="brand">
      <div class="brand__mark" aria-hidden="true"></div>
      <div class="brand__text">
        <span class="brand__name">The Harborline<br>Group</span>
        <span class="brand__tagline">Capital partner and growth studio<br>for bold, fast-scaling ventures</span>
      </div>
    </section>

    <div class="contact-icons" aria-hidden="true">
      <svg style="left:105px" width="18" height="26" viewBox="0 0 18 26">
        <rect x="1.5" y="1.5" width="15" height="23" rx="2" fill="none" stroke="var(--brand-blue)" stroke-width="2.5"/>
        <rect x="5" y="5" width="8" height="13" fill="var(--brand-blue)" opacity=".35"/>
      </svg>
      <svg style="left:430px; top:4px" width="28" height="20" viewBox="0 0 28 20">
        <rect x="1" y="1" width="26" height="18" fill="var(--brand-blue)"/>
        <path d="M1 1 L14 11 L27 1" fill="none" stroke="var(--white)" stroke-width="1.6"/>
      </svg>
      <svg style="left:740px" width="22" height="26" viewBox="0 0 22 26">
        <g fill="none" stroke="var(--brand-blue)" stroke-width="3" stroke-linecap="round">
          <path d="M9 14 L5 18 a4 4 0 0 0 6 6 L15 20"/>
          <path d="M13 12 L17 8 a4 4 0 0 0 -6 -6 L7 6"/>
          <path d="M8 17 L14 9"/>
        </g>
      </svg>
    </div>

    <footer class="contact-band">
      <span class="contact-band__item contact-band__phone">+1 628 307 4190</span>
      <span class="contact-band__item contact-band__email">peter@theharborlinegroup.com</span>
      <span class="contact-band__item contact-band__web">www.theharborlinegroup.com</span>
    </footer>
  </main>
</body>
</html>
```